K7 Solutions business card design contest. Use logo and create a professional layout.

See attached sample. Please sharpen all text and images, don't want any pix-elated content. We are looking for a clean look that quickly provides the information need. Please include our information provided on the sample card. Please feel free to offer any design changes. Please only user the colors provided: #2D3539 & #FFA500. Do not prefer any images other than the K7 Logo

Target Market(s)

Construction, Architects, General Contractors, residential

Industry/Entity Type

Business

Contact Information for Business Card

Company logo, Name, email, fax & phone

Font styles to use
Other font styles liked:
• Josefin Slab

Requirements
Must have
• Name
• Phone & Fax #'s
• address
• Logo
• Website url: www.kq7solutions.example
Nice to have
• Font Colors #2D3539 & #FFA400
• We prefer a white background.

```html
<!DOCTYPE html>
<html lang="en">
<head>
<meta charset="utf-8">
<title>K7 Solutions Business Card</title>
<link rel="stylesheet" href="https://fonts.googleapis.com/css2?family=Fira+Sans:wght@400;600&family=Montserrat:wght@600&display=swap">
<style>
  :root {
    --backdrop: #a7a8ab;
    --card: #ffffff;
    --ink: #000000;
    --accent: #ea7135;
    --on-dark: #ffffff;
  }
  html, body {
    margin: 0;
    width: 1200px;
    height: 829px;
    overflow: hidden;
    background: var(--backdrop);
  }
  .business-card {
    position: absolute;
    left: 184px;
    top: 178px;
    width: 820px;
    height: 468px;
    display: block;
    filter: drop-shadow(2px 3px 3px rgba(0, 0, 0, 0.35));
  }
  .card-face { fill: var(--card); }
  .feature-area { fill: var(--ink); }
  .brand-mark { fill: var(--ink); }
  .brand-name {
    font-family: "Montserrat", sans-serif;
    font-weight: 600;
    font-size: 36px;
    fill: var(--ink);
  }
  .service-list {
    font-family: "Fira Sans", sans-serif;
    font-weight: 600;
    font-size: 27px;
    fill: var(--accent);
  }
  .contact-name {
    font-family: "Fira Sans", sans-serif;
    font-weight: 400;
    font-size: 25px;
    fill: var(--on-dark);
  }
  .contact-title {
    font-family: "Fira Sans", sans-serif;
    font-weight: 400;
    font-size: 16px;
    fill: var(--on-dark);
  }
  .contact-detail {
    font-family: "Fira Sans", sans-serif;
    font-weight: 400;
    font-size: 14px;
    fill: var(--on-dark);
  }
  .contact-label { font-weight: 600; }
</style>
</head>
<body>
<svg class="business-card" viewBox="0 0 683 390" xmlns="http://www.w3.org/2000/svg">
  <rect class="card-face" x="0" y="0" width="683" height="390"/>

  <path class="feature-area" role="img" aria-label="Large black hand graphic behind the contact details"
        d="M 250 160 L 683 160 L 683 390 L 250 390 C 214 390 187 362 187 326 L 187 224 C 187 188 214 160 250 160 Z"/>

  <rect class="brand-mark" x="48" y="42" width="64" height="64"/>
  <text class="brand-name" x="140" y="88">K7 Solutions</text>

  <text class="service-list" text-anchor="middle">
    <tspan x="92" y="240">Dron</tspan>
    <tspan x="92" y="283">Webcam</tspan>
    <tspan x="92" y="326">Video</tspan>
  </text>

  <text class="contact-name" x="542" y="212" text-anchor="end">Marcus D. Hollander, MBA</text>
  <text class="contact-title" x="542" y="237" text-anchor="end">Director of Operations</text>

  <text class="contact-detail" x="542" y="291" text-anchor="end"><tspan class="contact-label">Mobile : </tspan> (555) 318 - 4470</text>
  <text class="contact-detail" x="542" y="310" text-anchor="end"><tspan class="contact-label">Fax : </tspan>(555) 318 - 4471</text>
  <text class="contact-detail" x="542" y="338" text-anchor="end">2170 Lindenbrook Road, Suit 210-118</text>
  <text class="contact-detail" x="542" y="357" text-anchor="end">Ashford, Georgia, 30000</text>
</svg>
</body>
</html>
```